Orthopaedic Clinic Needs facebook page

Orthopaedic Clinic needs facebook page. The name of our clinic is Maple & Ridge Orthopaedics. We focus on hip and knee orthopaedic conditions, as well as general orthopaedics. The main services are total knee replacements, total hip replacements, sports injury of the knee, hip fractures. Unique selling points of our service would be 1. Patient Centred Care, 2. Value Driven, 3. 2 Double-Fellowship Trained Surgeons.

Colour scheme should fit the logo design and be within the general colour recommendations of a medical clinic.

The design should be modern, eye catching, draws the end user to the website.

We would like to design our facebook page for future social media marketing.
In accordance with local advertisement regulations pertaining to medical clinics, no statements must have any information or laudatory statements such as the use of best, better, breakthrough, champions, or any statements that imply superiority and that may create unjustified expectations of services.

Target Market(s)

Patients
Friends family and relatives of patients.

Font styles to use
Serif
Sans Serif

Requirements
Must have
• My project must have my logo.

A nice colour scheme comfortable to the eye.
Nice to have
• Nice eye catching design that will draw the end user to the page.
Should not have
• Must not have any information that create unjustified expectaions.
Must not contain laudatory statements such as best, better, breakthrough, champions, or other statement that may create unjustified expecation of services.

```html
<!DOCTYPE html>
<html lang="en">
<head>
<meta charset="utf-8">
<title>Maple &amp; Ridge Orthopaedics – Cover</title>
<link rel="stylesheet" href="https://fonts.googleapis.com/css2?family=Lexend+Exa:wght@300;400;500;600;700&display=swap">
<style>
  :root {
    --ink: #434d55;
    --teal: #5ab3ad;
    --navy: #0f2a33;
    --frame: #17343c;
    --caption: rgba(22, 52, 60, 0.94);
    --white: #ffffff;
  }
  * { margin: 0; padding: 0; box-sizing: border-box; }
  html, body { width: 1200px; height: 444px; overflow: hidden; background: var(--white); }
  .cover {
    position: relative; width: 1200px; height: 444px; background: var(--white);
    font-family: "Lexend Exa", sans-serif; color: var(--ink);
  }

  .brand { position: absolute; left: 16px; top: 20px; display: flex; align-items: center; gap: 18px; }
  .brand-mark { width: 84px; height: 88px; background: var(--teal); border-radius: 4px; }
  .brand-name { color: var(--ink); line-height: 1; text-transform: uppercase; font-weight: 400; }
  .brand-name .line-1 { display: block; font-size: 31px; letter-spacing: 0; white-space: nowrap; }
  .brand-name .line-2 { display: block; font-size: 22px; font-weight: 300; letter-spacing: 8.6px; margin-top: 12px; white-space: nowrap; }

  .services {
    position: absolute; left: 14px; top: 172px; width: 448px; height: 144px;
    border: 2px solid var(--navy); border-radius: 8px; padding: 21px 0 0 18px;
  }
  .services-title {
    position: absolute; top: -19px; left: 28px; background: var(--white); padding: 0 6px;
    color: var(--teal); font-weight: 600; font-size: 27px; line-height: 1.25; letter-spacing: 0;
  }
  .services-list { list-style: none; }
  .services-list li {
    position: relative; padding-left: 20px; font-size: 17px; font-weight: 400;
    color: var(--navy); letter-spacing: 0.2px; line-height: 26px; text-transform: uppercase; white-space: nowrap;
  }
  .services-list li::before {
    content: ""; position: absolute; left: 1px; top: 9px; width: 8px; height: 8px;
    border-radius: 50%; background: var(--teal);
  }

  .web-button {
    position: absolute; left: 92px; top: 374px; width: 292px; height: 30px;
    background: var(--navy); border-radius: 15px; color: var(--white);
    font-weight: 600; font-size: 10.5px; letter-spacing: 1.8px;
    display: flex; align-items: center; justify-content: center; text-transform: uppercase; white-space: nowrap;
  }

  .pillar {
    position: absolute; top: 12px; width: 228px; height: 422px;
    border: 3px solid var(--frame); overflow: hidden; background: var(--frame);
  }
  .pillar-1 { left: 490px; }
  .pillar-2 { left: 726px; }
  .pillar-3 { left: 960px; }
  .pillar-photo { position: absolute; inset: 0; }
  .pillar-1 .pillar-photo {
    background:
      radial-gradient(ellipse 70px 110px at 30px 170px, #5f9fce 0%, rgba(95,159,206,0) 100%),
      radial-gradient(ellipse 90px 120px at 160px 240px, #8fb8dc 0%, rgba(143,184,220,0) 100%),
      radial-gradient(ellipse 60px 80px at 140px 310px, #2f5a99 0%, rgba(47,90,153,0) 100%),
      linear-gradient(180deg, #eceff1 0%, #dde3e8 50%, #b8c6d2 100%);
  }
  .pillar-2 .pillar-photo {
    background:
      radial-gradient(ellipse 80px 140px at 40px 100px, #5b7fc4 0%, rgba(91,127,196,0) 100%),
      radial-gradient(ellipse 60px 90px at 50px 300px, #a06a52 0%, rgba(160,106,82,0) 100%),
      radial-gradient(ellipse 90px 90px at 160px 80px, #e9ecef 0%, rgba(233,236,239,0) 100%),
      linear-gradient(180deg, #5f83c6 0%, #4b6fb4 55%, #3a5a96 100%);
  }
  .pillar-3 .pillar-photo {
    background:
      radial-gradient(ellipse 100px 90px at 170px 40px, #f6cfc8 0%, rgba(246,207,200,0) 100%),
      radial-gradient(ellipse 70px 80px at 50px 240px, #e9eef3 0%, rgba(233,238,243,0) 100%),
      radial-gradient(ellipse 70px 110px at 200px 300px, #d9a47c 0%, rgba(217,164,124,0) 100%),
      linear-gradient(180deg, #f0d2cc 0%, #c8d6e4 45%, #9fb3c8 100%);
  }
  .pillar-caption {
    position: absolute; left: 0; right: 0; bottom: 0; height: 101px; background: var(--caption);
    display: flex; align-items: center; padding: 0 13px;
    color: var(--white); font-weight: 700; font-size: 20px; line-height: 27px;
    letter-spacing: 0; text-transform: uppercase; white-space: nowrap;
  }
  .pillar-3 .pillar-caption { font-size: 18px; line-height: 22px; }
</style>
</head>
<body>
<main class="cover">
  <header class="brand">
    <div class="brand-mark"></div>
    <h1 class="brand-name">
      <span class="line-1">Maple &amp; Ridge</span>
      <span class="line-2">Orthopaedics</span>
    </h1>
  </header>

  <section class="services">
    <h2 class="services-title">SERVICES</h2>
    <ul class="services-list">
      <li>Total Knee Replacements</li>
      <li>Total Hip Replacements</li>
      <li>Sports Injury of the Knee</li>
      <li>Hip Fractures</li>
    </ul>
  </section>

  <div class="web-button">www.mapleridgeortho.com</div>

  <article class="pillar pillar-1">
    <div class="pillar-photo" role="img" aria-label="Photo: physiotherapist assessing a patient's braced knee beside an exercise ball in a rehab gym"></div>
    <p class="pillar-caption">Patient<br>Centred<br>Care</p>
  </article>
  <article class="pillar pillar-2">
    <div class="pillar-photo" role="img" aria-label="Photo: clinician in blue scrubs kneeling to examine a patient's lower leg"></div>
    <p class="pillar-caption">Value<br>Driven</p>
  </article>
  <article class="pillar pillar-3">
    <div class="pillar-photo" role="img" aria-label="Photo: surgical team performing arthroscopic knee surgery in theatre"></div>
    <p class="pillar-caption">Double<br>Fellowship<br>Trained<br>Surgeons</p>
  </article>
</main>
</body>
</html>
```